We require a business card that promotes our Electrical business. Things we would like included are;
1) our business name, Bright Path Electrical and Communication
2) Our Electrical licence, EC 73620
3) Our ABN, 41 297 506 183
4) Our website, www.korvanelectric.com.au
5) Our Email, info@korvanelectric.com.au
6) Our contact number, 0462 158 704
7) Our address, 57 Larkfield Rd West Dunmore Perth 6109
8) Our logo, I will attach this (can you please change it so the ackground is white not black)
9) Our colours are red and white and perhaps some black
10) Managing Director Tomasz Relhuvan
11) the back to say 'notes' and have some lines for writing

Target Market(s)

General

Industry/Entity Type

Electrical

Contact Information for Business Card

Include the colour white, black and red.

Font styles to use
Sans Serif

Requirements
Nice to have
• A thunder bolt or a power point or a cord or something electrical, cartoon image of a cartoon like electrical tradie

```html
<!DOCTYPE html>
<html lang="en">
<head>
<meta charset="utf-8">
<title>Bright Path Electrical and Communication – Business Card</title>
<link rel="stylesheet" href="https://fonts.googleapis.com/css2?family=Lato:wght@400;700;900&display=swap">
<style>
  :root {
    --brand-red: #e0242b;
    --card-black: #060606;
    --card-white: #ffffff;
    --ink: #111111;
    --text-light: #e6e6e6;
    --backdrop: #ececec;
  }
  * { box-sizing: border-box; margin: 0; padding: 0; }
  html, body {
    width: 1200px;
    height: 863px;
    overflow: hidden;
    background: var(--backdrop);
    font-family: "Lato", Arial, sans-serif;
  }
  .card-set {
    position: absolute;
    left: 223px;
    top: 151px;
    display: flex;
    gap: 70px;
  }
  .card {
    position: relative;
    width: 342px;
    height: 560px;
    overflow: hidden;
    box-shadow: 0 10px 30px rgba(0,0,0,0.18);
  }

  /* Back: notes */
  .card-back { background: var(--card-white); }
  .notes-title {
    position: absolute;
    top: 48px;
    width: 100%;
    text-align: center;
    font-weight: 900;
    font-size: 38px;
    letter-spacing: 1px;
    color: var(--ink);
  }
  .notes-lines {
    position: absolute;
    left: 0;
    right: 0;
    top: 124px;
    list-style: none;
  }
  .notes-lines li {
    height: 42px;
    border-top: 2.5px solid var(--ink);
  }

  /* Front: details */
  .card-front { background: var(--card-black); color: var(--text-light); }
  .corner { position: absolute; }
  .corner-top { top: 0; right: 0; }
  .corner-bottom { bottom: 0; left: 0; }
  .front-content {
    position: absolute;
    top: 98px;
    left: 0;
    right: 0;
    text-align: center;
  }
  .brand-mark {
    width: 62px;
    height: 62px;
    margin: 0 auto 26px;
    border-radius: 50%;
    background: var(--brand-red);
  }
  .brand-name {
    font-weight: 900;
    font-size: 27px;
    letter-spacing: 1.5px;
    color: var(--card-white);
    line-height: 1;
  }
  .brand-tagline {
    font-size: 15px;
    margin-top: 4px;
    color: var(--text-light);
  }
  .person-name {
    margin-top: 18px;
    font-weight: 700;
    font-size: 21px;
    color: var(--brand-red);
  }
  .person-role {
    font-size: 17px;
    margin-top: 2px;
  }
  .detail-group {
    margin-top: 20px;
    font-size: 13px;
    line-height: 1.35;
  }
  .detail-group + .detail-group { margin-top: 16px; }
</style>
</head>
<body>
  <main class="card-set">
    <section class="card card-back" aria-label="Card back">
      <h2 class="notes-title">NOTES</h2>
      <ul class="notes-lines">
        <li></li><li></li><li></li><li></li><li></li>
        <li></li><li></li><li></li><li></li><li></li>
      </ul>
    </section>

    <section class="card card-front" aria-label="Card front">
      <svg class="corner corner-top" width="76" height="140" viewBox="0 0 76 140" aria-hidden="true">
        <polygon points="0,0 76,0 76,140" fill="var(--brand-red)"/>
      </svg>
      <svg class="corner corner-bottom" width="76" height="140" viewBox="0 0 76 140" aria-hidden="true">
        <polygon points="0,0 76,140 0,140" fill="var(--brand-red)"/>
      </svg>

      <div class="front-content">
        <div class="brand-mark" aria-hidden="true"></div>
        <h1 class="brand-name">BRIGHT PATH</h1>
        <p class="brand-tagline">Electrical and Communication</p>

        <p class="person-name">Tomasz Relhuvan</p>
        <p class="person-role">Managing Director</p>

        <div class="detail-group">
          <p>Electrical licence, EC 73620</p>
          <p>ABN, 41 297 506 183</p>
        </div>
        <div class="detail-group">
          <p>0462 158 704</p>
          <p>www.korvanelectric.com.au</p>
          <p>info@korvanelectric.com.au</p>
        </div>
        <div class="detail-group">
          <p>57 Larkfield Rd West</p>
          <p>Dunmore Perth 6109</p>
        </div>
      </div>
    </section>
  </main>
</body>
</html>
```